Business Card

We need some ideas for corporate business cards. I'm interested in a double sided card, with one side featuring our corporate logo, the other side with employee information.

Corporate colors, logo etc. available at www.brivalo.com

Industry/Entity Type

Business

Requirements
Must have
• The "Brivalo" logo with stylized "O"

Nice to have
• Preferred font is calibri

```html
<!DOCTYPE html>
<html lang="en">
<head>
<meta charset="utf-8">
<title>Brivalo Business Card</title>
<link href="https://fonts.googleapis.com/css2?family=Carlito:wght@400;700&display=swap" rel="stylesheet">
<style>
  :root {
    --backdrop: #6f6f6f;
    --brand-blue: #47639a;
    --ink-blue: #2c4c8c;
    --name-blue: #1f57a8;
    --card-white: #ffffff;
    --text-grey: #4a4a4a;
    --soft-grey: #777777;
  }
  * { margin: 0; padding: 0; box-sizing: border-box; }
  html, body { width: 1200px; height: 795px; overflow: hidden; }
  body {
    background: var(--backdrop);
    font-family: "Carlito", "Calibri", sans-serif;
    position: relative;
  }
  .card {
    position: absolute;
    top: 245px;
    width: 520px;
    height: 305px;
    border-radius: 22px;
    box-shadow: 0 10px 24px rgba(0,0,0,0.35);
  }
  .card-front { left: 50px; background: var(--brand-blue); }
  .card-back { left: 630px; background: var(--card-white); color: var(--text-grey); }

  .wordmark {
    position: absolute;
    display: flex;
    align-items: center;
    gap: 10px;
    font-weight: 700;
    letter-spacing: 3px;
    line-height: 1;
  }
  .wordmark .mark-square { display: block; }
  .card-front .wordmark {
    left: 50%; top: 50%;
    transform: translate(-50%, -50%);
    color: var(--card-white);
    font-size: 52px;
  }
  .card-front .mark-square { width: 30px; height: 30px; background: var(--card-white); }
  .card-back .wordmark {
    right: 34px; top: 38px;
    color: var(--ink-blue);
    font-size: 44px;
  }
  .card-back .mark-square { width: 25px; height: 25px; background: var(--ink-blue); }

  .person { position: absolute; left: 34px; top: 150px; }
  .person-name { color: var(--name-blue); font-size: 22px; font-weight: 700; }
  .person-role { font-size: 14px; margin-left: 88px; margin-top: -2px; }

  .contact { position: absolute; left: 34px; bottom: 26px; font-size: 12px; line-height: 1.45; }
  .office { position: absolute; left: 250px; top: 195px; font-size: 12px; line-height: 1.35; }
  .office-label { font-size: 11px; }
  .office-name { font-weight: 700; font-size: 14px; }
  .office-address { font-size: 14px; }

  .social { position: absolute; right: 30px; top: 140px; font-size: 12px; line-height: 1.6; text-align: right; }
  .social-item { display: flex; align-items: center; justify-content: flex-end; gap: 5px; }
  .social-item i { width: 9px; height: 9px; background: var(--soft-grey); display: inline-block; }
  .legal { position: absolute; right: 30px; top: 196px; font-size: 9px; line-height: 1.4; text-align: right; color: var(--text-grey); }
</style>
</head>
<body>
  <section class="card card-front" aria-label="Card front">
    <div class="wordmark"><span class="mark-square"></span><span>BRIVALO</span></div>
  </section>

  <section class="card card-back" aria-label="Card back">
    <div class="wordmark"><span class="mark-square"></span><span>BRIVALO</span></div>

    <div class="person">
      <p class="person-name">Harlow, Daniel</p>
      <p class="person-role">Director</p>
    </div>

    <div class="office">
      <p class="office-label">Head Office</p>
      <p class="office-name">Brivalo</p>
      <p class="office-address">45, Elm Street Singapore.</p>
    </div>

    <div class="social">
      <p class="social-item"><i></i>in/Brivalo</p>
      <p class="social-item"><i></i>Brivalo &nbsp;<i></i>/Brivalo</p>
    </div>

    <div class="legal">
      <p>12 Harbour Road, Westfield Business Park, Dublin</p>
      <p>All rights reserved © 2013.</p>
    </div>

    <div class="contact">
      <p>Mobile: +353 1 555 0142</p>
      <p>Mail: &nbsp;info@brivalo.com</p>
      <p>Website: www.brivalo.com</p>
    </div>
  </section>
</body>
</html>
```